Website for a dog poop removal service.

The Lawn Brigade specializes in professional and hassle-free pet waste removal services, ensuring your yard stays clean, fresh, and safe for your family and pets. We take care of the dirty work, so you don’t have to, offering reliable, scheduled cleanups tailored to your needs. Let us help you reclaim your time and enjoy a spotless, stress-free outdoor space!
We will need the winning website to be transferred to our domain located at Servlaro. We would like to have the following web pages.
Home
About
Services
Contact Us
Client Portal
FAQ
Blog
Free Quote
The Free Quote webpage and client portal will need to be integrated with the following our account on the following website: kelvatrack.com

```html
<!DOCTYPE html>
<html lang="en">
<head>
<meta charset="utf-8">
<title>The Lawn Brigade – Pet Waste Removal</title>
<link rel="stylesheet" href="https://fonts.googleapis.com/css2?family=Fredoka:wght@600;700&family=Nunito:wght@400;600;700;800&display=swap">
<style>
:root{
  --green:#6cb33f;
  --green-light:#8fc764;
  --orange:#e98f2e;
  --tan:#c79c74;
  --lavender:#e7ecfb;
  --ink:#1c1c1c;
  --text:#2b2b2b;
  --white:#ffffff;
  --peach:#fde3cf;
  --icon-blue:#dde6fb;
  --soft-grey:#f1f2f5;
}
*{box-sizing:border-box;margin:0;padding:0}
html,body{width:1200px;height:3992px;overflow:hidden}
body{position:relative;background:var(--white);font-family:"Nunito",sans-serif;color:var(--text)}
.abs{position:absolute}
.display{font-family:"Fredoka",sans-serif;font-weight:700;color:var(--ink);letter-spacing:.3px}
.ph{position:absolute}
a{color:inherit;text-decoration:none}

/* header + hero */
.hero-bg{left:0;top:0;width:1200px;height:708px;background:var(--lavender)}
.brand{display:flex;align-items:center;gap:12px;font-weight:800;font-size:26px;color:var(--ink)}
.brand-dot{width:54px;height:54px;border-radius:50%;background:var(--green)}
.nav{left:418px;top:44px;display:flex;align-items:center;gap:32px;font-size:14.5px;color:var(--ink)}
.nav-home{width:32px;height:32px;border-radius:50%;background:var(--white);display:flex;align-items:center;justify-content:center}
.btn{display:inline-flex;align-items:center;justify-content:center;border-radius:20px;color:var(--white);font-size:13.5px;font-weight:600}
.btn-orange{background:var(--orange)}
.btn-green{background:var(--green)}
.btn-tan{background:var(--tan)}
.hero-title{left:88px;top:204px;font-size:44px;line-height:46px}
.hero-sub{left:88px;top:352px;font-size:14.5px}
.hero-photo{left:606px;top:152px;width:504px;height:330px;border-radius:30px;background:linear-gradient(135deg,#9cc46a,#c6a06a 55%,#7fa84e)}

.features{left:228px;top:555px;width:882px;height:153px;background:var(--white);border-right:12px solid var(--green);border-radius:4px 0 0 0}
.feature{position:absolute;top:34px;font-family:"Fredoka",sans-serif;font-weight:600;font-size:16px;line-height:22px;color:var(--ink)}
.feature i{display:block;width:46px;height:46px;border-radius:50%;background:var(--peach);margin-bottom:12px}
.mascot{background:linear-gradient(180deg,var(--soft-grey) 0 70%,var(--green-light) 100%);border-radius:50% 50% 40% 40%}

/* about */
.about-photo{left:144px;top:800px;width:420px;height:420px;border-radius:50%;background:linear-gradient(160deg,#8a9aa8,#c9c3b6 50%,#6c8a44)}
.about-title{left:646px;top:870px;font-size:44px}
.about-text{left:648px;top:932px;width:415px;font-size:13.4px;line-height:19.5px}
.about-text p+p{margin-top:10px}

/* why */
.why-title{left:0;top:1268px;width:1200px;text-align:center;font-size:44px}
.why{position:absolute;top:1350px;width:230px;text-align:center}
.why-icon{width:156px;height:130px;margin:0 auto;background:#f3f5fb;display:flex;align-items:center;justify-content:center}
.why-icon span{width:120px;height:120px;border-radius:34px;background:var(--icon-blue);display:flex;align-items:center;justify-content:center}
.why-icon.hot span{background:var(--orange)}
.why h3{font-family:"Fredoka",sans-serif;font-weight:600;font-size:16.5px;margin-top:18px;color:var(--ink)}
.why p{font-size:13.5px;line-height:19px}

/* services */
.services-band{left:0;top:1560px;width:1200px;height:840px}
.services-title{left:0;top:1805px;width:1200px;text-align:center;font-size:44px;line-height:45px;color:var(--white)}
.card{position:absolute;top:1928px;width:248px;height:346px;background:var(--white);border-radius:18px;overflow:hidden}
.card-img{height:176px;margin:2px 12px 0;border-radius:0 0 22px 22px}
.card h3{font-family:"Fredoka",sans-serif;font-weight:600;font-size:16.5px;margin:32px 0 2px 26px;color:var(--ink)}
.card p{font-size:13.5px;line-height:19.5px;margin:0 20px 0 26px}

/* faq */
.faq-title{left:0;top:2436px;width:1200px;text-align:center;font-size:44px;line-height:45px}
.faq-q{display:inline-flex;width:44px;height:44px;border-radius:50%;background:var(--orange);color:var(--white);align-items:center;justify-content:center;font-size:32px;vertical-align:4px;margin-right:8px}
.tabs{left:0;top:2548px;width:1200px;display:flex;justify-content:center;gap:22px;font-family:"Fredoka",sans-serif;font-weight:600;font-size:13.5px;color:var(--ink)}
.tabs .on{color:var(--orange)}
.faq-list{left:520px;top:2643px;width:476px}
.faq-item{background:var(--lavender);border-radius:16px;padding:17px 28px;margin-bottom:10px;font-family:"Fredoka",sans-serif;font-weight:600;font-size:13.5px;color:var(--ink);display:flex;justify-content:space-between}
.faq-item b{color:var(--orange);font-size:18px;line-height:14px}
.faq-item.open{display:block;padding-bottom:26px}
.faq-item.open p{font-family:"Nunito",sans-serif;font-weight:400;font-size:13.5px;line-height:19px;margin-top:12px}
.faq-item.open .row{display:flex;justify-content:space-between}

/* contact */
.contact-title{left:170px;top:3120px;font-size:42px;line-height:44px}
.contact-text{left:171px;top:3272px;width:230px;font-size:13.5px;line-height:19.5px}
.arch{left:468px;top:3030px;width:256px;height:380px;border-radius:128px 128px 0 0;background:var(--peach)}
.contact-photo{left:430px;top:3090px;width:330px;height:370px;background:linear-gradient(180deg,#e8c8ad,#b88a60 60%,#8c7a6a);border-radius:140px 140px 20px 20px}
.contact-info{left:790px;top:3170px;font-family:"Fredoka",sans-serif;font-weight:600;font-size:19px;line-height:33px;color:var(--ink)}
.contact-info div{display:flex;align-items:flex-start;gap:10px}
.contact-info svg{margin-top:9px;flex:none}

/* footer */
.footer-bg{left:0;top:3505px;width:1200px;height:487px}
.footer-rule{left:90px;top:3678px;width:1020px;height:1px;background:#b9c3e3}
.to-top{left:580px;top:3658px;width:40px;height:40px;border-radius:50%;background:var(--ink);display:flex;align-items:center;justify-content:center}
.social{width:24px;height:24px;border-radius:5px;background:var(--ink)}
.foot-addr{left:156px;top:3712px;font-size:13.5px;line-height:25px}
.foot-nav{left:625px;top:3728px;display:flex;gap:27px;font-size:12.5px}
.cta-title{left:0;top:3800px;width:1200px;text-align:center;font-size:40px}
.copy{left:0;top:3940px;width:1200px;text-align:center;font-size:12.5px}
</style>
</head>
<body>

<!-- header & hero -->
<div class="abs hero-bg"></div>
<a class="abs brand" style="left:86px;top:32px" href="#"><span class="brand-dot"></span>The Lawn Brigade</a>
<nav class="abs nav">
  <span class="nav-home"><svg width="14" height="14" viewBox="0 0 14 14"><path d="M7 1 1 6.5h2V13h3V9h2v4h3V6.5h2z" fill="#6cb33f"/></svg></span>
  <a href="#">About</a><a href="#">Services</a><a href="#">Client Portal</a><a href="#">FAQ</a><a href="#">Blog</a><a href="#">Contact Us</a>
</nav>
<a class="abs btn btn-orange" style="left:988px;top:40px;width:122px;height:36px" href="#">Free Quote</a>

<h1 class="abs display hero-title">Keeping Your Yard<br>Clean, Fresh, and<br>Hassle-Free!</h1>
<p class="abs hero-sub">Professional pet waste removal services tailored to your needs.</p>
<a class="abs btn btn-green" style="left:88px;top:388px;width:204px;height:38px" href="#">Get a Free Quote Today!</a>
<a class="abs btn btn-tan" style="left:299px;top:388px;width:250px;height:38px" href="#">Schedule Your First Cleanup Now!</a>
<div class="ph hero-photo" role="img" aria-label="Photo of a family sitting on the lawn with their golden retriever"></div>

<div class="abs features">
  <div class="feature" style="left:82px"><i style="background:#e3f0d6"></i>Reliable, scheduled<br>cleanups</div>
  <div class="feature" style="left:297px"><i></i>Safe for pets<br>and family</div>
  <div class="feature" style="left:465px"><i></i>Affordable and<br>hassle-free</div>
  <div class="feature" style="left:672px"><i style="background:#ececec"></i>Environmentally<br>responsible disposal</div>
</div>
<div class="ph mascot" style="left:84px;top:512px;width:180px;height:208px" role="img" aria-label="Cartoon dog mascot holding a pooper scooper"></div>

<!-- about -->
<div class="ph about-photo" role="img" aria-label="Photo of a man mowing the lawn beside a white dog"></div>
<h2 class="abs display about-title">About</h2>
<div class="abs about-text">
  <p>We’re passionate about making life easier for pet owners. Our professional team is dedicated to ensuring your yard stays clean, healthy, and stress-free. With flexible scheduling, affordable rates, and top-notch customer service, we make pet ownership even more enjoyable.</p>
  <p>The Lawn Brigade specializes in professional and hassle-free pet waste removal services, ensuring your yard stays clean, fresh, and safe for your family and pets. We take care of the dirty work, so you don’t have to, offering reliable, scheduled cleanups tailored to your needs. Let us help you reclaim your time and enjoy a spotless, stress-free outdoor space!</p>
</div>

<!-- why choose us -->
<h2 class="abs display why-title">Why Choose Us?</h2>
<div class="why" style="left:117px"><div class="why-icon"><span><svg width="52" height="52" viewBox="0 0 52 52" fill="none" stroke="#1c1c1c" stroke-width="2"><path d="M26 4 8 10v14c0 12 8 20 18 24 10-4 18-12 18-24V10z"/><path d="M18 24h6l2-8c3 0 3 3 2 6h7c2 0 3 2 2 4l-2 8c0 1-1 2-3 2H18z"/></svg></span></div><h3>Reliable Service</h3><p>Always on time, always<br>thorough.</p></div>
<div class="why" style="left:345px"><div class="why-icon hot"><span><svg width="60" height="60" viewBox="0 0 60 60" fill="none" stroke="#fff" stroke-width="2.2"><circle cx="30" cy="22" r="13"/><circle cx="25" cy="20" r="1.5" fill="#fff"/><circle cx="35" cy="20" r="1.5" fill="#fff"/><path d="M30 36v16M30 46c-6-6-14-4-16 0 6 4 12 2 16 0zM30 46c6-6 14-4 16 0-6 4-12 2-16 0z"/></svg></span></div><h3>Pet &amp; Eco-Friendly</h3><p>Safe disposal methods and<br>eco-conscious practices.</p></div>
<div class="why" style="left:594px"><div class="why-icon"><span><svg width="56" height="56" viewBox="0 0 56 56" fill="none" stroke="#1c1c1c" stroke-width="2"><rect x="4" y="6" width="48" height="20" rx="3"/><path d="M12 12l2 4h4l-3 3 1 4-4-2-4 2 1-4-3-3h4zM28 12l2 4h4l-3 3 1 4-4-2-4 2 1-4-3-3h4zM44 12l2 4h4l-3 3 1 4-4-2-4 2 1-4-3-3h4z"/><path d="M18 34h6l3-8c3 0 3 4 2 8h8c2 0 3 2 2 4l-2 10c0 1-1 2-3 2H18z"/></svg></span></div><h3>Satisfaction Guaranteed</h3><p>We’re not happy unless<br>you’re happy!</p></div>
<div class="why" style="left:841px"><div class="why-icon"><span><svg width="56" height="56" viewBox="0 0 56 56" fill="none" stroke="#1c1c1c" stroke-width="2"><path d="M28 6a12 12 0 0 0-12 12c0 10 12 22 12 22s12-12 12-22A12 12 0 0 0 28 6z"/><circle cx="28" cy="18" r="4"/><ellipse cx="28" cy="44" rx="20" ry="6"/></svg></span></div><h3>Locally Owned &amp; Operated</h3><p>Supporting our community,<br>one yard at a time.</p></div>

<!-- services -->
<svg class="abs services-band" viewBox="0 0 1200 840" role="img" aria-label="Green lawn band with a grass edge and faint paw prints">
  <defs><linearGradient id="lawn" x1="0" y1="0" x2="0" y2="1"><stop offset="0" stop-color="#ffffff"/><stop offset=".22" stop-color="#8fc764"/><stop offset=".3" stop-color="#6cb33f"/></linearGradient></defs>
  <path d="M0 0 H1200 V840 C1000 760 200 760 0 830 Z" fill="url(#lawn)"/>
</svg>
<h2 class="abs display services-title">Our Services Tailored<br>to Your Needs</h2>
<div class="card" style="left:90px"><div class="card-img" style="background:linear-gradient(150deg,#b7a98a,#7d8c4e)" role="img" aria-label="Photo of a person bagging dog waste on the grass"></div><h3>Weekly Cleanups</h3><p>Keep your yard spotless with our regular cleanup services. Ideal for maintaining a fresh and clean outdoor space.</p></div>
<div class="card" style="left:347px"><div class="card-img" style="background:linear-gradient(150deg,#5a7a3a,#3a4a7a 60%,#6f8f3f)" role="img" aria-label="Photo of a gloved hand picking up after a black dog"></div><h3>One-Time Cleanups</h3><p>Need help before a special event or after a busy week? We’ve got you covered with our one-time cleanup service.</p></div>
<div class="card" style="left:604px"><div class="card-img" style="background:linear-gradient(150deg,#c9c2b8,#8a6e55)" role="img" aria-label="Photo of a person using a laptop with a dog nearby"></div><h3>Custom Schedules</h3><p>Choose a schedule that fits your lifestyle. We offer flexible options to ensure your yard stays pristine.</p></div>
<div class="card" style="left:861px"><div class="card-img" style="background:linear-gradient(150deg,#d9c9b0,#a58d6f)" role="img" aria-label="Photo of a woman holding a small white dog outdoors"></div><h3>Commercial Services</h3><p>Perfect for parks, apartment complexes, and other dog-friendly spaces. Let us handle the mess while you focus on your property.</p></div>

<!-- faq -->
<h2 class="abs display faq-title"><span class="faq-q">?</span>FAQ for Our Dog Poop<br>Removal Service</h2>
<div class="abs tabs"><span class="on">General Questions</span><span>Service Details</span><span>Pricing and Payments</span><span>Health and Safety</span><span>Customer Concerns</span><span>Additional Services</span></div>
<div class="ph mascot" style="left:204px;top:2598px;width:306px;height:356px" role="img" aria-label="Cartoon dog mascot holding a pooper scooper"></div>
<div class="abs faq-list">
  <div class="faq-item">What does your dog poop removal service include?<b>+</b></div>
  <div class="faq-item">Do you service all yard sizes?<b>+</b></div>
  <div class="faq-item">How often can I schedule your services?<b>+</b></div>
  <div class="faq-item open"><div class="row">Are you environmentally friendly?<b>–</b></div><p>Yes, we use biodegradable bags and ensure proper disposal of all waste to minimize environmental impact.</p></div>
</div>

<!-- contact -->
<h2 class="abs display contact-title">Let’s Keep<br>Your Yard<br>Clean!</h2>
<p class="abs contact-text">Ready to schedule your cleanup or have questions? We’d love to hear from you.</p>
<div class="abs arch"></div>
<div class="ph contact-photo" role="img" aria-label="Photo of a woman playing with three dogs"></div>
<div class="abs contact-info">
  <div><svg width="14" height="18" viewBox="0 0 14 18"><path d="M7 0a7 7 0 0 0-7 7c0 5 7 11 7 11s7-6 7-11a7 7 0 0 0-7-7zm0 10a3 3 0 1 1 0-6 3 3 0 0 1 0 6z" fill="#e98f2e"/></svg><span>4820 W Meadowlark Ln.<br>Boise, ID &nbsp;83709</span></div>
  <div><svg width="16" height="16" viewBox="0 0 16 16"><path d="M3 1l3 3-2 2c1 2 3 4 5 5l2-2 3 3-2 3C6 15 1 10 1 3z" fill="#e98f2e"/></svg><span>(208) 555-0147</span></div>
  <div><svg width="16" height="13" viewBox="0 0 16 13"><rect width="16" height="13" rx="2" fill="#e98f2e"/><path d="M1 2l7 5 7-5" stroke="#fff" stroke-width="1.5" fill="none"/></svg><span>info@thelawnbrigade.com</span></div>
</div>

<!-- footer -->
<svg class="abs footer-bg" viewBox="0 0 1200 487" preserveAspectRatio="none"><path d="M0 40 C300 0 900 0 1200 40 V487 H0 Z" fill="var(--lavender)"/></svg>
<a class="abs brand" style="left:156px;top:3568px" href="#"><span class="brand-dot"></span>The Lawn Brigade</a>
<span class="abs social" style="left:955px;top:3596px"></span>
<span class="abs social" style="left:998px;top:3596px;border-radius:50%"></span>
<div class="abs footer-rule"></div>
<a class="abs to-top" href="#"><svg width="12" height="8" viewBox="0 0 12 8"><path d="M1 7l5-5 5 5" stroke="#fff" stroke-width="2" fill="none"/></svg></a>
<div class="abs foot-addr">4820 W Meadowlark Ln. Boise, ID &nbsp;83709<br>(208) 555-0147 &nbsp;&nbsp;&nbsp;&nbsp;&nbsp;info@thelawnbrigade.com</div>
<nav class="abs foot-nav"><a href="#">About</a><a href="#">Services</a><a href="#">Client Portal</a><a href="#">FAQ</a><a href="#">Blog</a><a href="#">Contact Us</a></nav>
<h2 class="abs display cta-title">Are you ready to get started?</h2>
<a class="abs btn btn-orange" style="left:539px;top:3864px;width:122px;height:36px" href="#">Free Quote</a>
<p class="abs copy">© 2025 &nbsp; | &nbsp; The Lawn Brigade . All rights reserved.</p>

</body>
</html>
```